ROVA Pty Ltd Business Card

Looking for a simple yet eye-catching double-sided business card design using my company logo on one side and contact details on the other.

Target Market(s)

Government

Industry/Entity Type

Communication Systems Engineering

Contact Information for Business Card

ROVA Pty Ltd

Requirements
Nice to have
• Would be great to have a QR code so details can be scanned into contacts

```html
<!DOCTYPE html>
<html lang="en">
<head>
<meta charset="utf-8">
<title>ROVA Pty Ltd Business Card</title>
<link href="https://fonts.googleapis.com/css2?family=Open+Sans:wght@400;600;700&display=swap" rel="stylesheet">
<style>
  :root {
    --backdrop: #242424;
    --paper: #ffffff;
    --slate: #36424a;
    --ink: #1e2428;
    --band-text: #ffffff;
  }
  * { margin: 0; padding: 0; box-sizing: border-box; }
  html, body { width: 1200px; height: 780px; overflow: hidden; }
  body {
    background: var(--backdrop);
    font-family: "Open Sans", Arial, sans-serif;
    position: relative;
  }
  .card {
    position: absolute;
    left: 290px;
    width: 620px;
    height: 344px;
    background: var(--paper);
    overflow: hidden;
  }
  .card--front { top: 30px; }
  .card--back { top: 406px; }

  .brand {
    position: absolute;
    display: flex;
    align-items: center;
    color: var(--slate);
    font-weight: 700;
    letter-spacing: 0.04em;
    line-height: 1;
  }
  .brand__dot {
    border-radius: 50%;
    background: var(--slate);
    flex: none;
  }
  .card--front .brand {
    left: 0; right: 0; top: 136px;
    justify-content: center;
    gap: 26px;
    font-size: 76px;
  }
  .card--front .brand__dot { width: 56px; height: 56px; }

  .card--back .brand {
    left: 196px; top: 52px;
    gap: 18px;
    font-size: 52px;
  }
  .card--back .brand__dot { width: 38px; height: 38px; }

  .person {
    position: absolute;
    right: 340px;
    top: 172px;
    text-align: right;
    color: var(--slate);
  }
  .person__name { font-size: 24px; font-weight: 700; line-height: 1.1; }
  .person__role { font-size: 14px; font-weight: 400; color: var(--ink); }

  .divider {
    position: absolute;
    left: 300px; top: 150px;
    width: 2px; height: 88px;
    background: var(--ink);
  }

  .contacts {
    position: absolute;
    left: 318px; top: 150px;
    list-style: none;
    color: var(--ink);
    font-size: 15px;
    line-height: 27px;
  }
  .contacts li { display: flex; align-items: center; gap: 10px; }
  .contacts svg { width: 14px; height: 14px; fill: var(--slate); flex: none; }

  .band { position: absolute; inset: 0; }
  .band__fill { fill: var(--slate); }
  .band__swoosh { fill: none; stroke: var(--slate); stroke-width: 3; }

  .address {
    position: absolute;
    left: 0; right: 0; bottom: 14px;
    text-align: center;
    color: var(--band-text);
    font-size: 15px;
    letter-spacing: 0.02em;
  }
</style>
</head>
<body>
  <section class="card card--front" aria-label="Card front">
    <div class="brand"><span class="brand__dot"></span><span class="brand__name">ROVA</span></div>
  </section>

  <section class="card card--back" aria-label="Card back">
    <svg class="band" viewBox="0 0 620 344" preserveAspectRatio="none" aria-hidden="true">
      <path class="band__swoosh" d="M0,289 Q360,279 620,200"/>
      <path class="band__fill" d="M0,300 Q360,290 620,215 L620,344 L0,344 Z"/>
    </svg>

    <div class="brand"><span class="brand__dot"></span><span class="brand__name">ROVA</span></div>

    <div class="person">
      <p class="person__name">Jordan Hale</p>
      <p class="person__role">Co-Founder</p>
    </div>

    <div class="divider"></div>

    <ul class="contacts">
      <li>
        <svg viewBox="0 0 24 24" aria-hidden="true"><path d="M6.6 10.8a15.1 15.1 0 0 0 6.6 6.6l2.2-2.2a1 1 0 0 1 1-.25 11.4 11.4 0 0 0 3.6.57 1 1 0 0 1 1 1V20a1 1 0 0 1-1 1A17 17 0 0 1 3 4a1 1 0 0 1 1-1h3.5a1 1 0 0 1 1 1c0 1.25.2 2.45.57 3.57a1 1 0 0 1-.25 1z"/></svg>
        <span>(555) 014-3826</span>
      </li>
      <li>
        <svg viewBox="0 0 24 24" aria-hidden="true"><path d="M12 2a10 10 0 1 0 0 20 10 10 0 0 0 0-20zm6.9 6h-2.9a15.7 15.7 0 0 0-1.4-3.6A8 8 0 0 1 18.9 8zM12 4c.8 1.2 1.5 2.5 1.9 4h-3.8c.4-1.5 1.1-2.8 1.9-4zM4.3 14a8 8 0 0 1 0-4h3.4a16 16 0 0 0 0 4zm.8 2h2.9c.3 1.3.8 2.5 1.4 3.6A8 8 0 0 1 5.1 16zM8 8H5.1a8 8 0 0 1 4.3-3.6C8.8 5.5 8.3 6.7 8 8zm4 12c-.8-1.2-1.5-2.5-1.9-4h3.8c-.4 1.5-1.1 2.8-1.9 4zm2.3-6H9.7a14.6 14.6 0 0 1 0-4h4.6a14.6 14.6 0 0 1 0 4zm.3 5.6c.6-1.1 1.1-2.3 1.4-3.6h2.9a8 8 0 0 1-4.3 3.6zm1.7-5.6a16 16 0 0 0 0-4h3.4a8 8 0 0 1 0 4z"/></svg>
        <span>www.rova.com.au</span>
      </li>
      <li>
        <svg viewBox="0 0 24 24" aria-hidden="true"><path d="M3 5h18a1 1 0 0 1 1 1v12a1 1 0 0 1-1 1H3a1 1 0 0 1-1-1V6a1 1 0 0 1 1-1zm1 2.4V17h16V7.4l-8 5.3z M5.5 7 12 11.3 18.5 7z"/></svg>
        <span>admin@rova.com.au</span>
      </li>
    </ul>

    <p class="address">42-44 Harbour Lane Eastmere NSW 2999 Australia</p>
  </section>
</body>
</html>
```